Hotel Morvi Bar Menu and Cafe Menu

I would like to Revise and Modify my existing Menu for My Hotel Morvi .1) One side is Bar Menu2) One side is Food Menu .All The Attachment has File Name to Understand Better. I have attached 3 Diff Files for Bar Menu and 3 Diff File for Food Menu which i have done in Past also i am Attaching Back ground Image i have used for the Bar Menu. also i am attaching Bar Menu New Price and Food Menu New Price which i want to Add on your New design. also i am adding some of the Food Images which i have used for Previous Designalso On Bar Menu i would like to Add some of the Images in small size Next to " Morvi Specialty Cocktails "the Images i would like too Add Next to Truly Fine Mojito , Felix at Dawn , Silver Gate , Blue Lagoon Cocktail ETC , you don't have to add But try to Add at least 3 Images in Morvi Specialty Cocktail section. i would like to ADD on Both Menu Food and Bar Menu at the Bottom of the page i Have Address Phone number Below that i would like to Add "Open : Tuesday to Saturday From 4: 30 to 10: 30 Close : Sunday and Monday
Updates

Went on vacation/holiday

Industry/Entity Type

Hospitality

Font styles to use
Serif
Sans Serif
Decorative
Script

Requirements
Must have
• 2 Bar Menu:
• 1st one with address on the Bottom :
• Hotel Morvi
• 7431 Pembrin Ave
• North Hollywood CA 91601
• Ph: 1 555 304 7129
• with Green , Chartreuse Green Black and Blue and Purple kind of Color Theme
• and
• 2nd Menu with Address :
• Hotel Morvi
• 18652 Quillmoor Ave
• Newhall , CA 91321
• with Orange , Chartreuse Green Black and Blue and Purple kind of Color Theme
• and
• Hours Open: 4:30 to 10:30 Thursday to Saturday
• Close: Sunday and Monday
• the color Theme for the 2 nd Bar menu is Orange.
Nice to have
• 2 Bar Menu:
• Hotel Morvi
• 7431 Pembrin Ave
• Ph: 1 555 304 7129
• and
• 2nd Menu with Address :
• Hotel Morvi
• 18652 Quillmoor Ave
• Newhall , CA 91321
• and

```html
<!DOCTYPE html>
<html lang="en">
<head>
<meta charset="utf-8">
<title>Morvi Cafe Food Menu</title>
<link rel="stylesheet" href="https://fonts.googleapis.com/css2?family=Acme&family=Roboto+Condensed:wght@400&family=Arimo:wght@400;700&display=swap">
<style>
  :root {
    --page-bg: #e7e2da;
    --lime: #a6d23f;
    --lime-light: #d6eca0;
    --lime-pale: #e4f3bd;
    --title-green: #9ccf3c;
    --royal-blue: #1c4aa0;
    --ink: #1f1f1f;
    --footer-black: #222224;
    --white: #ffffff;
    --rule: #eef8d6;
  }
  * { margin: 0; padding: 0; box-sizing: border-box; }
  html, body { width: 1200px; height: 1200px; overflow: hidden; background: var(--page-bg); }
  .menu {
    position: absolute; left: 151px; top: 20px;
    width: 897px; height: 1160px;
    background: var(--lime);
    box-shadow: 0 4px 14px rgba(0,0,0,0.25);
    overflow: hidden;
  }
  .header-photo {
    position: absolute; left: 0; top: 0; width: 100%; height: 352px;
    background:
      radial-gradient(ellipse 40% 30% at 35% 45%, rgba(232,214,178,0.85) 0%, rgba(232,214,178,0) 100%),
      radial-gradient(ellipse 30% 25% at 75% 55%, rgba(150,170,200,0.7) 0%, rgba(150,170,200,0) 100%),
      linear-gradient(180deg, #6fa3da 0%, #a9c6e6 22%, #dcc8a8 42%, #b87a62 62%, #8a5a48 76%, #4f6a3a 100%);
  }
  .top-trim {
    position: absolute; left: 0; top: 0; width: 100%; height: 16px;
    background: linear-gradient(180deg, var(--lime) 0%, var(--lime-light) 100%);
  }
  .title {
    position: absolute; right: 18px; font-family: "Acme", sans-serif; font-weight: 400;
    text-align: right; line-height: 1; text-shadow: 0 2px 3px rgba(0,0,0,0.45);
  }
  .title-cafe { top: 18px; font-size: 64px; color: var(--title-green); }
  .title-menu { top: 84px; font-size: 50px; color: var(--white); }
  .blue-band {
    position: absolute; left: 0; top: 352px; width: 100%; height: 12px;
    background: var(--royal-blue);
  }
  .body-panel {
    position: absolute; left: 0; top: 364px; width: 100%; height: 573px;
    background: radial-gradient(ellipse at 50% 35%, #e8f5c6 0%, #c6e381 45%, var(--lime) 100%);
  }
  .dish-frame {
    position: absolute; width: 294px; height: 294px; border-radius: 50%;
    background: radial-gradient(circle, var(--lime-pale) 80%, var(--lime-light) 100%);
    display: flex; align-items: center; justify-content: center;
  }
  .dish-photo { width: 254px; height: 254px; border-radius: 50%; box-shadow: 0 0 0 3px rgba(255,255,255,0.5); }
  .dish-burger { background: radial-gradient(circle at 50% 40%, #d99a4a 0%, #a0652e 35%, #6b4a2e 65%, #2e2622 100%); }
  .dish-fish { background: radial-gradient(circle at 55% 42%, #f1e6c6 0%, #dcc894 38%, #b7b090 58%, #3f6b2c 88%); }
  .dish-pizza { background: radial-gradient(circle at 50% 50%, #eba458 0%, #cf5a34 50%, #8e3520 100%); }
  .price-list {
    position: absolute; top: 722px; width: 348px;
    font-family: "Roboto Condensed", sans-serif; font-size: 16px; color: var(--ink);
    list-style: none;
  }
  .price-list.left { left: 54px; }
  .price-list.right { left: 461px; }
  .price-item {
    display: flex; align-items: baseline; height: 44.6px; padding-top: 11px;
    border-bottom: 2px solid var(--rule);
    white-space: nowrap;
  }
  .price-item::before { content: "•"; margin-right: 5px; }
  .leader { flex: 1; border-bottom: 2px dotted var(--ink); margin: 0 2px 4px; }
  .bottom-trim {
    position: absolute; left: 0; top: 934px; width: 100%; height: 16px;
    background: linear-gradient(180deg, var(--lime) 0%, #5f8fb8 60%, var(--royal-blue) 100%);
  }
  .footer {
    position: absolute; left: 0; top: 950px; width: 100%; height: 210px;
    background: var(--footer-black);
  }
  .hotel-name {
    position: absolute; left: 44px; top: 14px; width: 300px;
    font-family: "Arimo", sans-serif; font-weight: 400; color: var(--white);
    text-align: center; line-height: 1;
  }
  .hotel-name .line-top { display: block; font-size: 46px; letter-spacing: 14px; margin-bottom: 22px; }
  .hotel-name .line-main { display: block; font-size: 74px; letter-spacing: 4px; }
  .info {
    position: absolute; left: 403px; top: 14px;
    font-family: "Arimo", sans-serif; font-weight: 700; line-height: 1;
  }
  .info p { white-space: nowrap; }
  .hours { font-size: 27.5px; color: var(--title-green); margin-bottom: 9px; }
  .days { font-size: 27.5px; color: var(--white); margin-bottom: 9px; }
  .contact { font-size: 33.5px; color: var(--title-green); margin-bottom: 9px; }
  .address { font-size: 22.5px; font-weight: 400; color: var(--white); }
</style>
</head>
<body>
  <main class="menu">
    <div class="header-photo" role="img" aria-label="Street view of the hotel building with shops and trees"></div>
    <div class="top-trim"></div>
    <h1 class="title title-cafe">Morvi Cafe</h1>
    <h2 class="title title-menu">Food Menu</h2>
    <div class="blue-band"></div>

    <section class="body-panel"></section>

    <div class="dish-frame" style="left:9px; top:386px;"><div class="dish-photo dish-burger" role="img" aria-label="Chicken burger photo"></div></div>
    <div class="dish-frame" style="left:302px; top:386px;"><div class="dish-photo dish-fish" role="img" aria-label="Cod fish fillet with greens photo"></div></div>
    <div class="dish-frame" style="left:592px; top:386px;"><div class="dish-photo dish-pizza" role="img" aria-label="Pizza with olives and peppers photo"></div></div>

    <ul class="price-list left">
      <li class="price-item">Daily Harvest Salad ( Veggie or Chicken )<span class="leader"></span>$8</li>
      <li class="price-item">Shoe Strings Fries<span class="leader"></span>$6</li>
      <li class="price-item">Morvi Wings ( 7 Pieces )<span class="leader"></span>$10</li>
      <li class="price-item">Sriracha Chicken Bites<span class="leader"></span>$13</li>
    </ul>
    <ul class="price-list right">
      <li class="price-item">Chees Quesadilla ( Veggie or Chicken )<span class="leader"></span>$9</li>
      <li class="price-item">Cod Fish Fillet (Craft Beer Battered with Fries )<span class="leader"></span>$13</li>
      <li class="price-item">Morvi Burger ( Veggie, Chicken with Fries)<span class="leader"></span>$13</li>
      <li class="price-item">Pizza (Veggie or Pepperoni )<span class="leader"></span>$13</li>
    </ul>

    <div class="bottom-trim"></div>

    <footer class="footer">
      <div class="hotel-name"><span class="line-top">HOTEL</span><span class="line-main">MORVI</span></div>
      <div class="info">
        <p class="hours">Hours Open: 4:30 to 10:30</p>
        <p class="days">Thursday to Saturday</p>
        <p class="days">Close: Sunday and Monday</p>
        <p class="contact">Contact us : 1 555 304 7129</p>
        <p class="address">7431 Pembrin Ave, North Hollywood CA 91601</p>
      </div>
    </footer>
  </main>
</body>
</html>
```